BRC Business cards

We are a medium sized property company based in London and require a logo, Business card which reflects a professional company and incorporates our catchy name.

Our statement is (Building for the future) we like colours such as royal blue, greens and light browns but will look at anything.

Contact Information for Business Card

Brookcrest Estates Limited
Unit 4, 15-17 Farrowby Lane
London
SE22 7QN

Web: www.brookcrestestates-example.com

Email: brookcrestltd@mailbox-example.com

Telephone: +44-208-555-0142
Fax: +44-208-555-0187

```html
<!DOCTYPE html>
<html lang="en">
<head>
<meta charset="utf-8">
<title>Brookcrest Estates Limited – Business Card</title>
<link rel="stylesheet" href="https://fonts.googleapis.com/css2?family=Arimo:wght@400;700&display=swap">
<style>
  :root {
    --page-white: #ffffff;
    --leaf-green: #80c35f;
    --royal-blue: #193782;
    --block-blue: #0059a5;
    --ink-navy: #1c3c8c;
  }
  html, body {
    margin: 0;
    padding: 0;
    width: 1200px;
    height: 695px;
    overflow: hidden;
    background: var(--page-white);
  }
  .canvas {
    position: relative;
    width: 1200px;
    height: 695px;
    background: var(--page-white);
    font-family: "Arimo", Arial, sans-serif;
  }
  .card {
    position: absolute;
    left: 59px;
    top: 3px;
    width: 1084px;
    height: 687px;
    background: var(--leaf-green);
    overflow: hidden;
  }
  .card__band {
    position: absolute;
    left: 0;
    top: 0;
  }
  .brand {
    position: absolute;
    left: 0;
    top: 0;
    width: 100%;
    height: 334px;
    display: flex;
    align-items: center;
    justify-content: center;
    gap: 26px;
  }
  .brand__mark {
    flex: none;
    width: 48px;
    height: 48px;
    background: var(--block-blue);
  }
  .brand__name {
    margin: 0;
    color: var(--leaf-green);
    font-weight: 700;
    font-size: 52px;
    line-height: 1;
    white-space: nowrap;
  }

  .contact {
    position: absolute;
    left: 249px;
    top: 388px;
    margin: 0;
    color: var(--ink-navy);
    font-size: 31px;
    font-weight: 400;
    line-height: 42px;
    font-style: normal;
  }
  .contact__address { margin: 0 0 26px 0; }
  .contact__list {
    list-style: none;
    margin: 0;
    padding: 0;
  }
  .contact__label {
    display: inline-block;
    width: 58px;
  }
</style>
</head>
<body>
  <div class="canvas">
    <section class="card" aria-label="Brookcrest Estates Limited business card">
      <svg class="card__band" width="1084" height="334" viewBox="0 0 1084 334" aria-hidden="true">
        <polygon points="83,0 1000,0 1084,85 1084,334 0,334 0,85" fill="var(--royal-blue)"/>
      </svg>

      <div class="brand">
        <span class="brand__mark" aria-hidden="true"></span>
        <p class="brand__name">Brookcrest Estates Limited</p>
      </div>

      <address class="contact">
        <p class="contact__address">Brookcrest Estates Limited<br>Unit 4, 15-17 Farrowby Lane, London SE22 7QN</p>
        <ul class="contact__list">
          <li><span class="contact__label">W :</span>www.brookcrestestates-example.com</li>
          <li><span class="contact__label">E :</span>brookcrestltd@mailbox-example.com</li>
          <li><span class="contact__label">T :</span>+44-208-555-0142</li>
          <li><span class="contact__label">F :</span>+44-208-555-0187</li>
        </ul>
      </address>
    </section>
  </div>
</body>
</html>
```